perch 17 design

We are needing a website built for our company. We are based in the Dallas/Ft. Worth area providing staging for realtors, occupied staging, apartments, builders and hospitality industry ( Kip Nests .) Have been in the design and furniture industry for 35+ years, looking to expand our services to the area. Here Are some of the buzzword used for staging. Turn properties into dream spaces. Staging preparing property for sale.
Design services offered for new construction . We want to incorporate our tag line Turning you property into a dream Space .
Industry/Entity Type
interior and home design
Coding
Coded - Design and coding required
Number of Pages Required
2 page

```html
<!DOCTYPE html>
<html lang="en">
<head>
<meta charset="utf-8">
<title>Perch 17 Design – Home Staging</title>
<link href="https://fonts.googleapis.com/css2?family=IBM+Plex+Sans:wght@400;500;600;700&family=Poppins:wght@600;700&display=swap" rel="stylesheet">
<style>
:root{
  --blue:#0b52b0;
  --blue-dark:#08448f;
  --ink:#1c1c1c;
  --text:#555;
  --muted:#777;
  --light:#f4f5f7;
  --white:#fff;
  --cta:#2b3540;
}
*{box-sizing:border-box;margin:0;padding:0}
html,body{width:1200px;height:4594px;overflow:hidden}
body{font-family:"IBM Plex Sans",Arial,sans-serif;color:var(--ink);background:var(--white);position:relative}
a{color:inherit;text-decoration:none}

/* header */
.site-header{position:absolute;top:0;left:0;width:1200px;height:128px;background:var(--white)}
.brand{position:absolute;left:134px;top:22px;width:120px;text-align:center;color:var(--ink);font-weight:700;line-height:1}
.brand .name{font-size:30px;letter-spacing:1px;display:block}
.brand .sub{font-size:10px;letter-spacing:3px;display:block;margin-top:6px}
.top-contact{position:absolute;top:24px;display:flex;align-items:center;gap:14px}
.top-contact svg{width:38px;height:30px}
.top-contact .sep{width:3px;height:38px;background:var(--blue)}
.top-contact .lbl{font-size:13px;font-weight:500;color:var(--ink)}
.top-contact .val{font-size:17px;color:var(--blue)}
.email{left:618px}
.call{left:866px}
.main-nav{position:absolute;top:79px;left:389px;display:flex;align-items:center;gap:0}
.main-nav a{font-size:13.5px;font-weight:500;padding:7px 12px;border-radius:16px;margin-right:12px;color:#222}
.main-nav a.active{background:var(--blue);color:var(--white)}

/* hero */
.hero{position:absolute;top:128px;left:0;width:1200px;height:578px;background:linear-gradient(180deg,#d9d6d0 0%,#c8c2b8 45%,#8a7767 100%)}
.hero h1{position:absolute;top:72px;width:100%;text-align:center;font-family:Poppins,sans-serif;font-weight:700;font-size:39px;line-height:48px;color:var(--white);letter-spacing:.5px}
.btn{display:inline-block;background:var(--blue);color:var(--white);font-weight:600;border-radius:22px}
.hero .btn{position:absolute;left:526px;top:190px;font-size:17px;padding:10px 24px}
.dots{position:absolute;top:535px;left:572px;display:flex;gap:10px}
.dots span{width:12px;height:12px;border-radius:50%;background:var(--white)}
.dots span.on{background:var(--blue)}

/* headings */
.sec-title{position:absolute;width:100%;text-align:center;font-size:26px;font-weight:600;letter-spacing:.3px}
.sec-title::after{content:"";display:block;width:36px;height:3px;background:var(--blue);margin:16px auto 0}

/* services */
.services{position:absolute;top:706px;left:0;width:1200px;height:867px;background:linear-gradient(180deg,#f6f6f7,#eeeff1)}
.card{position:absolute;background:var(--white);box-shadow:0 4px 18px rgba(0,0,0,.07)}
.card .photo{background:linear-gradient(135deg,#cfc9bf,#8d8377)}
.card h3{font-size:15px;font-weight:600;letter-spacing:.3px;margin-bottom:10px}
.card p{font-size:11.5px;line-height:17.5px;color:var(--text)}
.card .btn{font-size:10px;padding:6px 16px;margin-top:18px}
.card.tall{width:294px;height:373px;top:121px}
.card.tall .photo{height:182px}
.card.tall .body{padding:24px 28px}
.card.wide{width:457px;height:291px;top:524px;display:flex}
.card.wide .photo{width:207px;height:291px;flex:none}
.card.wide .body{padding:40px 28px 0 29px}

/* welcome */
.welcome{position:absolute;top:1573px;left:0;width:1200px;height:486px}
.welcome .panel{position:absolute;left:0;top:0;width:594px;height:486px;background:var(--blue);color:var(--white);padding:60px 60px 0 132px}
.welcome h2{font-size:26px;font-weight:600}
.welcome h2::after{content:"";display:block;width:36px;height:3px;background:var(--white);margin-top:18px}
.welcome p{font-size:15px;line-height:22.5px;margin-top:32px}
.welcome .btn{background:var(--white);color:var(--blue);font-size:10.5px;padding:7px 18px;margin-top:34px}
.welcome .photo{position:absolute;left:594px;top:0;width:606px;height:486px;background:linear-gradient(160deg,#e8e4de,#a59b90 60%,#6c6660)}

/* gallery */
.gallery{position:absolute;top:2059px;left:0;width:1200px;height:687px}
.gallery .grid{position:absolute;top:136px;left:21px;width:1165px;display:grid;grid-template-columns:repeat(4,1fr);gap:13px 12px}
.gallery .grid div{height:251px}
.g1{background:linear-gradient(160deg,#eceff2,#2c3d5a)}
.g2{background:linear-gradient(160deg,#e6e2dc,#3e3a36)}
.g3{background:linear-gradient(160deg,#b9b2aa,#2f2b28)}
.g4{background:linear-gradient(160deg,#6a4a36,#b95e3e)}
.g5{background:linear-gradient(160deg,#3a2e28,#7b8a5a)}
.g6{background:linear-gradient(160deg,#2d3a5c,#c8c3bd)}
.g7{background:linear-gradient(160deg,#4b3a2e,#2a2c33)}
.g8{background:linear-gradient(160deg,#2e3b2c,#b4a58e)}

/* why */
.why{position:absolute;top:2746px;left:0;width:1200px;height:624px;background:linear-gradient(180deg,#f4f4f5,#eceded)}
.why .feature-photo{position:absolute;left:455px;top:125px;width:294px;height:449px;border-radius:90px;background:linear-gradient(170deg,#6a4e38,#2b3b33 45%,#a3714a)}
.feature{position:absolute;width:290px;display:flex;gap:20px;padding-bottom:20px}
.feature.line{border-bottom:1px solid #d9d9d9}
.feature .ic{width:70px;height:70px;border-radius:50%;background:var(--blue);flex:none;display:flex;align-items:center;justify-content:center}
.feature .ic svg{width:34px;height:34px;fill:none;stroke:var(--white);stroke-width:2}
.feature h4{font-size:15px;font-weight:600;letter-spacing:.3px;margin-bottom:6px}
.feature p{font-size:11.5px;line-height:17.5px;color:var(--muted)}
.l{left:132px}.r{left:781px}

/* testimonials */
.testimonials{position:absolute;top:3370px;left:0;width:1200px;height:599px}
.tcell{position:absolute;width:297px;height:193px}
.tcell.ph1{background:linear-gradient(160deg,#5a4a3e,#2c2a2c)}
.tcell.ph2{background:linear-gradient(160deg,#efece8,#4a4f58)}
.tcell.ph3{background:linear-gradient(160deg,#e3e1dc,#3b3a3a)}
.quote{text-align:center;padding:10px 8px 0}
.quote .mark{font-family:Georgia,serif;font-style:italic;font-size:34px;color:var(--blue);line-height:30px}
.quote p{font-size:13.5px;line-height:19.5px;color:var(--text);margin-top:10px}
.quote .who{font-size:13.5px;color:var(--blue);margin-top:16px;letter-spacing:.5px}

/* cta */
.cta{position:absolute;top:3969px;left:0;width:1200px;height:269px;background:linear-gradient(180deg,#3a444f,#1f2731);color:var(--white);text-align:center}
.cta h2{font-size:25.5px;font-weight:600;line-height:39px;margin-top:52px;letter-spacing:.3px}
.cta .btn{background:var(--white);color:var(--blue);font-size:13px;padding:9px 18px;margin-top:20px;border-radius:18px}

/* footer */
.site-footer{position:absolute;top:4238px;left:0;width:1200px;height:356px;background:var(--blue);color:var(--white)}
.site-footer .brand{color:var(--white);top:92px;left:132px;width:118px}
.fcol{position:absolute;top:42px}
.fcol h5{font-size:14px;font-weight:600;letter-spacing:.3px;padding-bottom:10px;border-bottom:2px solid var(--white)}
.fcol.contact{left:351px;width:194px}
.fcol.menu{left:694px;width:108px}
.fcol.follow{left:959px;width:108px}
.fitem{display:flex;align-items:center;gap:14px;font-size:11.5px;line-height:14px;margin-top:24px}
.fitem .dot{width:24px;height:24px;border-radius:50%;background:var(--white);flex:none;display:flex;align-items:center;justify-content:center}
.fitem .dot svg{width:13px;height:13px;fill:var(--blue)}
.fcol.follow .fitem{margin-top:26px;gap:12px}
.menu ul{list-style:none;margin-top:16px}
.menu li{font-size:11.5px;line-height:19px}
.site-footer .rule{position:absolute;left:132px;top:273px;width:934px;height:2px;background:var(--white)}
.site-footer .copy{position:absolute;top:312px;width:100%;text-align:center;font-size:11px}
</style>
</head>
<body>

<header class="site-header">
  <a class="brand" href="#"><span class="name">PERCH 17</span><span class="sub">DESIGN</span></a>
  <div class="top-contact email">
    <svg viewBox="0 0 38 30" fill="none" stroke="#0b52b0" stroke-width="2"><rect x="12" y="6" width="22" height="16" rx="2"/><path d="M12 7l11 9 11-9"/><path d="M2 10h7M4 15h6M2 20h8"/></svg>
    <span class="sep"></span>
    <div><div class="lbl">EMAIL US</div><div class="val">info@Perch17.com</div></div>
  </div>
  <div class="top-contact call">
    <svg viewBox="0 0 30 30" fill="none" stroke="#0b52b0" stroke-width="2"><path d="M7 4l5 1 2 6-3 2a14 14 0 0 0 7 7l2-3 6 2 1 5c-1 2-3 3-5 3C12 27 3 18 4 8c0-2 1-3 3-4z"/><path d="M18 4a8 8 0 0 1 8 8M18 9a3 3 0 0 1 3 3"/></svg>
    <span class="sep"></span>
    <div><div class="lbl">CALL US</div><div class="val">+1 555 017 0117</div></div>
  </div>
  <nav class="main-nav">
    <a class="active" href="#">HOME</a><a href="#">ABOUT US</a><a href="#">SERVICES</a><a href="#">PORTFOLIO</a><a href="#">TESTIMONIALS</a><a href="#">BLOG</a><a href="#">CONTACT</a>
  </nav>
</header>

<section class="hero" role="img" aria-label="Bright staged living room with fireplace, sofa and tall windows">
  <h1>TURNING YOUR PROPERTY<br>INTO A DREAM SPACE</h1>
  <a class="btn" href="#">READ MORE</a>
  <div class="dots"><span></span><span class="on"></span><span></span></div>
</section>

<section class="services">
  <h2 class="sec-title" style="top:38px">OUR SERVICES</h2>
  <article class="card tall" style="left:132px">
    <div class="photo" role="img" aria-label="Realtors showing a home to a couple"></div>
    <div class="body"><h3>REALTORS</h3><p>Lorem ipsum dolor sit amet, conse ctetur adipiscing elit, sed do eiusmod tempor incididunt ut labore et dolore magna aliqua</p><a class="btn" href="#">READ MORE</a></div>
  </article>
  <article class="card tall" style="left:453px">
    <div class="photo" role="img" aria-label="Staged home office with desk and plants"></div>
    <div class="body"><h3>OCCUPIED STAGING</h3><p>Lorem ipsum dolor sit amet, conse ctetur adipiscing elit, sed do eiusmod tempor incididunt ut labore et dolore magna aliqua</p><a class="btn" href="#">READ MORE</a></div>
  </article>
  <article class="card tall" style="left:774px">
    <div class="photo" role="img" aria-label="Apartment living room with white sofas"></div>
    <div class="body"><h3>APARTMENTS</h3><p>Lorem ipsum dolor sit amet, conse ctetur adipiscing elit, sed do eiusmod tempor incididunt ut labore et dolore magna aliqua</p><a class="btn" href="#">READ MORE</a></div>
  </article>
  <article class="card wide" style="left:132px">
    <div class="photo" role="img" aria-label="New construction living area with stone fireplace"></div>
    <div class="body"><h3>BUILDERS</h3><p>Lorem ipsum dolor sit amet, conse ctetur adipiscing elit, sed do eius mod tempor incididunt ut labore et dolore magna aliqua aliquip ex ea commodo cons equat. Duis aute irure dolor in reprehenderit in voluptate velit esse cillum dolore eu fugiat nulla pariatur.</p><a class="btn" href="#">READ MORE</a></div>
  </article>
  <article class="card wide" style="left:613px">
    <div class="photo" role="img" aria-label="Colourful hospitality lounge with patterned wall"></div>
    <div class="body"><h3>HOSPITALITY INDUSTRY</h3><p>Lorem ipsum dolor sit amet, conse ctetur adipiscing elit, sed do eius mod tempor incididunt ut labore et dolore magna aliqua aliquip ex ea commodo cons equat. Duis aute irure dolor in reprehenderit in voluptate velit esse cillum dolore eu fugiat nulla pariatur.</p><a class="btn" href="#">READ MORE</a></div>
  </article>
</section>

<section class="welcome">
  <div class="panel">
    <h2>WELCOME TO PERCH17</h2>
    <p>At vero eos et accusamus et iusto odio dignissimos ducimus qui blanditiis praesentium voluptatum deleniti atque corrupti quos dolores et quas molestias excepturi sint occaecati cupiditate non provident, similique sunt in culpa qui officia deserunt mollitia animi, id est laborum et dolorum fuga. Et harum quidem rerum facilis est et expedita distinctio. Nam libero tempore, cum soluta nobis est eligendi optio cumque nihil impedit quo</p>
    <a class="btn" href="#">READ MORE</a>
  </div>
  <div class="photo" role="img" aria-label="Staged bedroom with tufted headboard and dark dressers"></div>
</section>

<section class="gallery">
  <h2 class="sec-title" style="top:46px">TAKE A LOOK AT OUR HOME STAGING WORK</h2>
  <div class="grid">
    <div class="g1" role="img" aria-label="White kitchen island with pendant lights"></div>
    <div class="g2" role="img" aria-label="Living room with tall windows"></div>
    <div class="g3" role="img" aria-label="Sitting area with round table"></div>
    <div class="g4" role="img" aria-label="Bed with striped pillows"></div>
    <div class="g5" role="img" aria-label="Leaf and vase decor on a table"></div>
    <div class="g6" role="img" aria-label="Bedroom with bunk beds"></div>
    <div class="g7" role="img" aria-label="Lounge with leather sofa and hide rug"></div>
    <div class="g8" role="img" aria-label="Patio with hanging chair and candles"></div>
  </div>
</section>

<section class="why">
  <h2 class="sec-title" style="top:40px">WHY CHOOSE PERCH17</h2>
  <div class="feature-photo" role="img" aria-label="Game room with pool table and wooden ceiling"></div>

  <div class="feature l line" style="top:125px">
    <div class="ic"><svg viewBox="0 0 34 34"><rect x="5" y="10" width="24" height="17" rx="2"/><path d="M13 10V7h8v3M5 17h24M17 15v4"/></svg></div>
    <div><h4>EXPERIENCED</h4><p>Lorem ipsum dolor sit amet, conse ctetur adipiscing elit, sed do eius mod tempor incididunt ut labore et dolore magna aliqua aliquip ex ea commodo cons equat.</p></div>
  </div>
  <div class="feature l line" style="top:287px">
    <div class="ic"><svg viewBox="0 0 34 34"><rect x="8" y="7" width="10" height="21"/><rect x="18" y="13" width="8" height="15"/><path d="M11 11h4M11 15h4M11 19h4M21 17h2M21 21h2M5 28h24"/></svg></div>
    <div><h4>ESTABLISHED BUSINESS</h4><p>Lorem ipsum dolor sit amet, conse ctetur adipiscing elit, sed do eius mod tempor incididunt ut labore et dolore magna aliqua aliquip ex ea commodo cons equat.</p></div>
  </div>
  <div class="feature l" style="top:453px">
    <div class="ic"><svg viewBox="0 0 34 34"><circle cx="17" cy="11" r="5"/><path d="M7 28c0-6 4-10 10-10s10 4 10 10M17 18v6"/></svg></div>
    <div><h4>PROFESSIONAL STAFF</h4><p>Lorem ipsum dolor sit amet, conse ctetur adipiscing elit, sed do eius mod tempor incididunt ut labore et dolore magna aliqua aliquip ex ea commodo cons equat.</p></div>
  </div>

  <div class="feature r line" style="top:125px">
    <div class="ic"><svg viewBox="0 0 34 34"><rect x="8" y="7" width="18" height="22" rx="2"/><path d="M13 7V5h8v2M12 14h2M16 14h7M12 19h2M16 19h7M12 24h2M16 24h7"/></svg></div>
    <div><h4>EXPANSIVE INVENTORY</h4><p>Lorem ipsum dolor sit amet, conse ctetur adipiscing elit, sed do eius mod tempor incididunt ut labore et dolore magna aliqua aliquip ex ea commodo cons equat.</p></div>
  </div>
  <div class="feature r line" style="top:287px">
    <div class="ic"><svg viewBox="0 0 34 34"><path d="M9 5h12l5 5v10M9 5v24h10"/><path d="M13 12h8M13 16h8M13 20h4"/><circle cx="24" cy="25" r="4"/><path d="M22 25l1.5 1.5 2.5-3"/></svg></div>
    <div><h4>ACCREDITED</h4><p>Lorem ipsum dolor sit amet, conse ctetur adipiscing elit, sed do eius mod tempor incididunt ut labore et dolore magna aliqua aliquip ex ea commodo cons equat.</p></div>
  </div>
  <div class="feature r" style="top:453px">
    <div class="ic"><svg viewBox="0 0 34 34"><path d="M17 4l11 4v8c0 7-5 12-11 14C11 28 6 23 6 16V8z"/><circle cx="17" cy="17" r="5"/><path d="M15 17l1.5 1.5 3-3"/></svg></div>
    <div><h4>RELIABLE</h4><p>Lorem ipsum dolor sit amet, conse ctetur adipiscing elit, sed do eius mod tempor incididunt ut labore et dolore magna aliqua aliquip ex ea commodo cons equat.</p></div>
  </div>
</section>

<section class="testimonials">
  <h2 class="sec-title" style="top:64px">TESTIMONIALS</h2>
  <div class="tcell ph1" style="left:132px;top:146px" role="img" aria-label="Living room with dark sofa and hide rug"></div>
  <div class="tcell quote" style="left:451px;top:146px">
    <div class="mark">“</div>
    <p>Lorem ipsum dolor sit amet, conse ctetur adipiscing elit, sed do eius mod tempor incididunt ut labore et dolore magna aliqua aliquip ex ea commodo cons equat.</p>
    <div class="who">DANA WELLS</div>
  </div>
  <div class="tcell ph2" style="left:774px;top:146px" role="img" aria-label="Living room with stone fireplace and tall windows"></div>
  <div class="tcell quote" style="left:132px;top:341px">
    <div class="mark">“</div>
    <p>Lorem ipsum dolor sit amet, conse ctetur adipiscing elit, sed do eius mod tempor incididunt ut labore et dolore magna aliqua aliquip ex ea commodo cons equat.</p>
    <div class="who">DANA WELLS</div>
  </div>
  <div class="tcell ph3" style="left:451px;top:341px" role="img" aria-label="Bright bathroom with vanity and shower"></div>
  <div class="tcell quote" style="left:774px;top:341px">
    <div class="mark">“</div>
    <p>Lorem ipsum dolor sit amet, conse ctetur adipiscing elit, sed do eius mod tempor incididunt ut labore et dolore magna aliqua aliquip ex ea commodo cons equat.</p>
    <div class="who">DANA WELLS</div>
  </div>
</section>

<section class="cta" role="img" aria-label="Dusk city skyline of the Dallas/Ft. Worth area">
  <h2>CONTACT US FOR PREMIER STAGING<br>SERVICES IN THE DALLAS/FT. WORTH AREA</h2>
  <a class="btn" href="#">CONTACT US</a>
</section>

<footer class="site-footer">
  <a class="brand" href="#"><span class="name">PERCH 17</span><span class="sub">DESIGN</span></a>
  <div class="fcol contact">
    <h5>CONTACT US</h5>
    <div class="fitem"><span class="dot"><svg viewBox="0 0 14 14"><path d="M7 1a4 4 0 0 0-4 4c0 3 4 8 4 8s4-5 4-8a4 4 0 0 0-4-4zm0 5.5A1.5 1.5 0 1 1 7 3.5a1.5 1.5 0 0 1 0 3z"/></svg></span><span>412 Harbor Ln, Millbrook,<br>ON K0L 2T5, Canada</span></div>
    <div class="fitem"><span class="dot"><svg viewBox="0 0 14 14"><path d="M3 1l2.5.5 1 3-1.5 1a7 7 0 0 0 3.5 3.5l1-1.5 3 1L13 11c-.5 1-1.5 2-2.5 2C5.5 13 1 8.5 1 3.5 1 2.5 2 1.5 3 1z"/></svg></span><span>Call Us<br>+1 555 017 0117</span></div>
    <div class="fitem"><span class="dot"><svg viewBox="0 0 14 14"><path d="M1 3h12v8H1zM1 3l6 5 6-5" fill="none" stroke="#0b52b0" stroke-width="1.4"/></svg></span><span>E mail Us<br>info@Perch17.com</span></div>
  </div>
  <div class="fcol menu">
    <h5>MENU</h5>
    <ul><li>HOME</li><li>ABOUT US</li><li>SERVICES</li><li>PORTFOLIO</li><li>TESTIMONIALS</li><li>BLOG</li><li>CONTACT</li></ul>
  </div>
  <div class="fcol follow">
    <h5>FOLLOW US</h5>
    <div class="fitem"><span class="dot"></span><span>Like us on<br>CIRCLEBOOK</span></div>
    <div class="fitem"><span class="dot"></span><span>Follow us on<br>CHIRPER</span></div>
    <div class="fitem"><span class="dot"></span><span>Follow us on<br>LINKWORK</span></div>
  </div>
  <div class="rule"></div>
  <div class="copy">Copyright © 2023 All Rights Reserved</div>
</footer>

</body>
</html>
```